Business Card Re-Design/Update

We'd like to update out business cards. I've included our current "Style guide" which has the colour scheme of the organisation in it. I've also included the branding files with logos etc in them.

I've also included a copy of one of our existing cards so that you can see how ugly/dated they look. I'd like a fresh modern corporate look.

Target Market(s)

These are for our clients, potential clients, industry contacts - like all business cards

Contact Information for Business Card

Name
Position
Company Address - Level 1, 47 Garnet Lane, Toowong Qld 4066
Direct Phone
mobile
Email
Website -www.korvalnet.com.au
Logo

Colors

Designer to choose colors to be used in the design.

Requirements
Must have
• Main Logo
• Cards will need to be editable to be able to personalize them for each new employee.
Nice to have
• The MapOUT, HandOVER, UpKEEP would be okay to have if they can be sensibly and professionally added to the look without detracting from the main imagery.
• Maybe they could go on the back of the card? will leave this to your creative discretion as to whether/where they fit.
Should not have
• Should not have decorative or script fonts

```html
<!DOCTYPE html>
<html lang="en">
<head>
<meta charset="utf-8">
<title>korvalnet business card</title>
<link href="https://fonts.googleapis.com/css2?family=Poppins:wght@400;500;600;700&display=swap" rel="stylesheet">
<style>
  :root {
    --red: #d71f26;
    --ink: #2a2a2a;
    --charcoal: #3a3b3d;
    --charcoal-deep: #232426;
    --paper: #ffffff;
    --backdrop: #1f2124;
    --muted: #4a4a4a;
  }
  * { margin: 0; padding: 0; box-sizing: border-box; }
  html, body {
    width: 1200px; height: 900px; overflow: hidden;
    background: var(--backdrop);
    font-family: "Poppins", Arial, sans-serif;
  }
  .sheet {
    width: 1200px; height: 900px;
    display: flex; align-items: center; justify-content: center; gap: 50px;
  }
  .card {
    position: relative; width: 530px; height: 303px;
    border-radius: 22px; overflow: hidden;
    box-shadow: 0 10px 30px rgba(0,0,0,.45);
  }

  /* Front */
  .card-front { background: var(--paper); color: var(--ink); }
  .front-band { position: absolute; left: 0; bottom: 0; width: 100%; height: 303px; }
  .person { position: absolute; left: 30px; top: 26px; }
  .person-name { color: var(--red); font-weight: 700; font-size: 20px; line-height: 1.1; }
  .person-role { font-size: 10.5px; color: var(--muted); font-weight: 500; }
  .contact { position: absolute; left: 30px; top: 80px; list-style: none; font-size: 10.5px; line-height: 1.6; color: var(--ink); white-space: nowrap; }
  .contact li { display: flex; align-items: center; gap: 7px; }
  .contact svg { width: 11px; height: 11px; flex: none; }
  .wordmark { position: absolute; display: flex; align-items: center; gap: 10px; font-weight: 500; letter-spacing: -0.5px; line-height: 1; }
  .wordmark-square { background: var(--red); flex: none; }
  .card-front .wordmark { right: 30px; top: 160px; font-size: 40px; color: var(--ink); }
  .card-front .wordmark-square { width: 30px; height: 30px; }
  .address { position: absolute; right: 30px; bottom: 36px; text-align: right; font-size: 13px; font-weight: 500; line-height: 1.45; color: var(--ink); }

  /* Back */
  .card-back { background: linear-gradient(160deg, var(--charcoal), var(--charcoal-deep)); }
  .back-band { position: absolute; left: 0; top: 0; width: 100%; height: 303px; }
  .card-back .wordmark { right: 34px; top: 62px; font-size: 46px; color: var(--paper); }
  .card-back .wordmark-square { width: 36px; height: 36px; }
  .services { position: absolute; left: 0; right: 0; bottom: 30px; display: flex; justify-content: space-around; padding: 0 18px; list-style: none; }
  .service { display: flex; align-items: center; gap: 6px; color: var(--paper); font-size: 17px; font-weight: 500; }
  .service-mark { width: 12px; height: 12px; border: 2px solid var(--paper); }
</style>
</head>
<body>
<main class="sheet">
  <section class="card card-front" aria-label="Card front">
    <svg class="front-band" viewBox="0 0 530 303" aria-hidden="true">
      <polygon points="250,252 265,280 530,280 530,303 230,303 230,252" fill="#d71f26"/>
      <polygon points="230,252 250,252 265,280 230,280" fill="#b5151c"/>
    </svg>
    <div class="person">
      <p class="person-name">Mara Ellison</p>
      <p class="person-role">Business Development Manager</p>
    </div>
    <ul class="contact">
      <li><svg viewBox="0 0 12 12"><rect x="3" y="1" width="6" height="10" rx="1" fill="none" stroke="#d71f26" stroke-width="1.3"/></svg>+61 (0)400 555 182 | D +61 (0)7 3055 0147</li>
      <li><svg viewBox="0 0 12 12"><path d="M2 2c1-1 2-1 2.5 0l1 2-1 1c.5 1.3 1.2 2 2.5 2.5l1-1 2 1c1 .5 1 1.5 0 2.5C7 11 1 5 2 2z" fill="#d71f26"/></svg>+61 (0)7 3055 0100 | F +61 (0)7 3055 0199</li>
      <li><svg viewBox="0 0 12 12"><rect x="1" y="2.5" width="10" height="7" rx="1" fill="#d71f26"/><path d="M1.5 3l4.5 3.5L10.5 3" fill="none" stroke="#fff" stroke-width="1"/></svg>mellison@korvalnet.com.au</li>
      <li><svg viewBox="0 0 12 12"><circle cx="6" cy="6" r="5" fill="#d71f26"/><path d="M1 6h10M6 1c2 2.5 2 7.5 0 10M6 1c-2 2.5-2 7.5 0 10" fill="none" stroke="#fff" stroke-width=".8"/></svg>www.korvalnet.com.au</li>
    </ul>
    <div class="wordmark"><span class="wordmark-square"></span><span>korvalnet</span></div>
    <p class="address">Level 1, 47 Garnet Lane<br>Toowong Qld 4066</p>
  </section>

  <section class="card card-back" aria-label="Card back">
    <svg class="back-band" viewBox="0 0 530 303" aria-hidden="true">
      <polygon points="0,165 430,225 530,225 530,303 0,303" fill="#d71f26"/>
      <polygon points="0,165 0,150 445,214 430,225" fill="#1a1b1d" opacity=".6"/>
    </svg>
    <div class="wordmark"><span class="wordmark-square"></span><span>korvalnet</span></div>
    <ul class="services">
      <li class="service"><span class="service-mark"></span>HandOVER</li>
      <li class="service"><span class="service-mark"></span>MapOUT</li>
      <li class="service"><span class="service-mark"></span>UpKEEP</li>
    </ul>
  </section>
</main>
</body>
</html>
```